Now Leasing Banner

Looking for a banner that says the following information approx 4' x 30'

Now Leasing Maplewood Terrace 925-318-6054

Target Market(s)

Drive by traffic

Industry/Entity Type

Residential property management

Requirements
Must have
• Clear and readable from a distance

```html
<!DOCTYPE html>
<html lang="en">
<head>
<meta charset="utf-8">
<title>Now Leasing – Maplewood Terrace</title>
<link rel="stylesheet" href="https://fonts.googleapis.com/css2?family=Russo+One&family=Michroma&display=swap">
<style>
  :root {
    --ink-green: #1b3d20;
    --leaf-green: #77c244;
    --lime: #d6e021;
    --paper: #ffffff;
  }
  html, body {
    margin: 0;
    padding: 0;
    width: 1200px;
    height: 160px;
    overflow: hidden;
    background: var(--paper);
  }
  .banner {
    display: block;
    width: 1200px;
    height: 160px;
  }
  .corner-lime { fill: var(--lime); }
  .corner-leaf { fill: var(--leaf-green); }
  .headline-kicker {
    font-family: "Russo One", sans-serif;
    font-size: 35px;
    fill: var(--ink-green);
  }
  .headline-name {
    font-family: "Russo One", sans-serif;
    font-size: 90px;
    fill: var(--ink-green);
    stroke: var(--paper);
    stroke-width: 7px;
    stroke-linejoin: round;
    paint-order: stroke fill;
  }
  .headline-phone {
    font-family: "Michroma", sans-serif;
    font-size: 24px;
    font-weight: 700;
    fill: var(--ink-green);
    stroke: var(--ink-green);
    stroke-width: 0.8px;
  }
</style>
</head>
<body>
<svg class="banner" viewBox="0 0 1200 160" xmlns="http://www.w3.org/2000/svg">
  <g class="corner corner-left">
    <polygon class="corner-lime" points="0,0 289,0 0,160"/>
    <polygon class="corner-leaf" points="0,0 217,0 0,154"/>
  </g>
  <g class="corner corner-right">
    <polygon class="corner-lime" points="908,0 1200,0 1200,160"/>
    <polygon class="corner-leaf" points="983,0 1200,0 1200,154"/>
  </g>

  <text class="headline-kicker" x="426" y="42" textLength="346" lengthAdjust="spacingAndGlyphs">NOW LEASING</text>
  <text class="headline-name" x="104" y="119" textLength="990" lengthAdjust="spacingAndGlyphs">MAPLEWOOD TERRACE</text>
  <text class="headline-phone" x="473" y="150" textLength="254" lengthAdjust="spacingAndGlyphs">925-318-6054</text>
</svg>
</body>
</html>
```